Email Signature

Hello,

We need an editable file so that when new staff start or someone is promoted we can easily edit this file.

The previous designer has not kept the email signatures uniform they should all be as per Garth Lindqvist signature.

I also need the Tomas Pirelli changes as below -
Senior Mechanical Engineer
Email should be tomas.pirelli@vantoq.com.au

You can see the Dale Okonkwo file is different I need this the same as Garth Lindqvist format but with details changed.

Also need a new one with details as per below -
Hugh Fenwick
Commercial Manager
0417 352 609
hugh.fenwick@vantoq.com.au
www.vantoq.com.au

```html
<!DOCTYPE html>
<html lang="en">
<head>
<meta charset="utf-8">
<title>Vantoq Email Signatures</title>
<link href="https://fonts.googleapis.com/css2?family=Barlow:wght@400;500;600;700&display=swap" rel="stylesheet">
<style>
  :root {
    --page-bg: #676767;
    --card-bg: #ffffff;
    --brand-blue: #14c2f0;
    --name-blue: #1ba2d6;
    --band-blue: #13a7d3;
    --band-green: #76b843;
    --text-dark: #3a3a3c;
    --deco-green: #edf5e5;
  }
  * { margin: 0; padding: 0; box-sizing: border-box; }
  html, body { width: 853px; height: 1200px; overflow: hidden; }
  body {
    background: var(--page-bg);
    font-family: "Barlow", sans-serif;
    position: relative;
  }
  .signature {
    position: absolute;
    left: 52px;
    width: 740px;
    height: 248px;
    background: var(--card-bg);
    overflow: hidden;
    box-shadow: 0 10px 12px -6px rgba(0,0,0,0.45);
  }
  .building-deco {
    position: absolute;
    left: 547px;
    top: 0;
    width: 193px;
    height: 210px;
    background:
      radial-gradient(ellipse 70% 80% at 45% 40%, rgba(226,240,214,0.9), rgba(226,240,214,0) 100%),
      linear-gradient(90deg, rgba(237,245,229,0) 0%, rgba(237,245,229,0.7) 25%, rgba(237,245,229,0.7) 80%, rgba(237,245,229,0) 100%);
  }
  .brand {
    position: absolute;
    left: 24px;
    top: 0;
    width: 336px;
    height: 206px;
    display: flex;
    align-items: center;
    justify-content: center;
    gap: 14px;
  }
  .brand-mark {
    width: 30px;
    height: 30px;
    background: var(--brand-blue);
    flex: none;
  }
  .brand-name {
    font-weight: 700;
    font-size: 58px;
    line-height: 1;
    color: var(--brand-blue);
  }
  .person {
    position: absolute;
    left: 411px;
    top: 22px;
  }
  .person-name {
    font-weight: 700;
    font-size: 34px;
    line-height: 1;
    color: var(--name-blue);
    text-transform: uppercase;
    white-space: nowrap;
  }
  .person-role {
    margin-top: 7px;
    font-weight: 600;
    font-size: 20px;
    line-height: 1;
    color: var(--text-dark);
    white-space: nowrap;
  }
  .contact-list {
    list-style: none;
    margin-top: 18px;
  }
  .contact-item {
    display: flex;
    align-items: center;
    height: 31.5px;
    font-size: 19.5px;
    font-weight: 500;
    color: var(--text-dark);
    white-space: nowrap;
  }
  .contact-icon {
    width: 20px;
    height: 20px;
    margin-right: 13px;
    flex: none;
  }
  .bands {
    position: absolute;
    left: 0;
    top: 0;
  }
  .hotline {
    position: absolute;
    left: 30px;
    top: 219px;
    display: flex;
    align-items: center;
    gap: 7px;
    font-weight: 600;
    font-size: 22px;
    line-height: 28px;
    color: #fff;
  }
  .hotline-number { margin-right: 11px; }
  .social-box {
    width: 16px;
    height: 16px;
    border-radius: 2px;
    background: #fff;
  }
  .address {
    position: absolute;
    left: 282px;
    top: 210px;
    display: flex;
    align-items: center;
    gap: 11px;
    font-weight: 600;
    font-size: 21px;
    line-height: 30px;
    color: #fff;
    white-space: nowrap;
  }
</style>
</head>
<body>

<svg width="0" height="0" style="position:absolute">
  <defs>
    <symbol id="icon-phone" viewBox="0 0 20 20">
      <circle cx="10" cy="10" r="10" fill="#1ba2d6"/>
      <path d="M6.5 5.5l2 -.5 1.2 2.6-1.3 1c.6 1.4 1.6 2.4 3 3l1-1.3 2.6 1.2-.5 2c-4.4.2-8.2-3.6-8-8z" fill="#fff"/>
    </symbol>
    <symbol id="icon-mail" viewBox="0 0 20 20">
      <circle cx="10" cy="10" r="10" fill="#1ba2d6"/>
      <rect x="5" y="6.5" width="10" height="7" rx="1" fill="#fff"/>
      <path d="M5.5 7.2l4.5 3.3 4.5-3.3" fill="none" stroke="#1ba2d6" stroke-width="1.1"/>
    </symbol>
    <symbol id="icon-web" viewBox="0 0 20 20">
      <circle cx="10" cy="10" r="10" fill="#1ba2d6"/>
      <circle cx="10" cy="10" r="5" fill="none" stroke="#fff" stroke-width="1.2"/>
      <ellipse cx="10" cy="10" rx="2.2" ry="5" fill="none" stroke="#fff" stroke-width="1"/>
      <path d="M5 10h10" stroke="#fff" stroke-width="1"/>
    </symbol>
    <symbol id="icon-pin" viewBox="0 0 20 20">
      <path d="M10 1.5c-3.6 0-6.3 2.7-6.3 6.2 0 4.5 6.3 10.8 6.3 10.8s6.3-6.3 6.3-10.8c0-3.5-2.7-6.2-6.3-6.2z" fill="#fff"/>
      <circle cx="10" cy="7.8" r="2.4" fill="#13a7d3"/>
    </symbol>
    <symbol id="signature-bands" viewBox="0 0 740 248">
      <polygon points="0,217 261,217 250,248 0,248" fill="#76b843"/>
      <polygon points="271,206 740,206 740,248 257,248" fill="#13a7d3"/>
    </symbol>
  </defs>
</svg>

<section class="signature" style="top:49px">
  <div class="building-deco" role="img" aria-label="Faint green city building illustration"></div>
  <div class="brand"><span class="brand-mark"></span><span class="brand-name">Vantoq</span></div>
  <div class="person">
    <h2 class="person-name">Dale Okonkwo</h2>
    <p class="person-role">DIRECTOR</p>
    <ul class="contact-list">
      <li class="contact-item"><svg class="contact-icon"><use href="#icon-phone"/></svg>0438 615207</li>
      <li class="contact-item"><svg class="contact-icon"><use href="#icon-mail"/></svg>dale.okonkwo@vantoq.com.au</li>
      <li class="contact-item"><svg class="contact-icon"><use href="#icon-web"/></svg>www.vantoq.com.au</li>
    </ul>
  </div>
  <svg class="bands" width="740" height="248"><use href="#signature-bands"/></svg>
  <div class="hotline"><span class="hotline-number">1300 462 318</span><span class="social-box"></span><span class="social-box"></span><span class="social-box"></span></div>
  <div class="address"><svg width="20" height="20"><use href="#icon-pin"/></svg>14/205 Carrick Road, Northgate QLD 4013</div>
</section>

<section class="signature" style="top:331px">
  <div class="building-deco" role="img" aria-label="Faint green city building illustration"></div>
  <div class="brand"><span class="brand-mark"></span><span class="brand-name">Vantoq</span></div>
  <div class="person">
    <h2 class="person-name">Tomas Pirelli</h2>
    <p class="person-role">Senior Mechanical Engineer</p>
    <ul class="contact-list">
      <li class="contact-item"><svg class="contact-icon"><use href="#icon-phone"/></svg>0455 213 874</li>
      <li class="contact-item"><svg class="contact-icon"><use href="#icon-mail"/></svg>tomas.pirelli@vantoq.com.au</li>
      <li class="contact-item"><svg class="contact-icon"><use href="#icon-web"/></svg>www.vantoq.com.au</li>
    </ul>
  </div>
  <svg class="bands" width="740" height="248"><use href="#signature-bands"/></svg>
  <div class="hotline"><span class="hotline-number">1300 462 318</span><span class="social-box"></span><span class="social-box"></span><span class="social-box"></span></div>
  <div class="address"><svg width="20" height="20"><use href="#icon-pin"/></svg>14/205 Carrick Road, Northgate QLD 4013</div>
</section>

<section class="signature" style="top:612px">
  <div class="building-deco" role="img" aria-label="Faint green city building illustration"></div>
  <div class="brand"><span class="brand-mark"></span><span class="brand-name">Vantoq</span></div>
  <div class="person">
    <h2 class="person-name">Garth Lindqvist</h2>
    <p class="person-role">Site Project Manager</p>
    <ul class="contact-list">
      <li class="contact-item"><svg class="contact-icon"><use href="#icon-phone"/></svg>0429 086 513</li>
      <li class="contact-item"><svg class="contact-icon"><use href="#icon-mail"/></svg>garth.lindqvist@vantoq.com.au</li>
      <li class="contact-item"><svg class="contact-icon"><use href="#icon-web"/></svg>www.vantoq.com.au</li>
    </ul>
  </div>
  <svg class="bands" width="740" height="248"><use href="#signature-bands"/></svg>
  <div class="hotline"><span class="hotline-number">1300 462 318</span><span class="social-box"></span><span class="social-box"></span><span class="social-box"></span></div>
  <div class="address"><svg width="20" height="20"><use href="#icon-pin"/></svg>14/205 Carrick Road, Northgate QLD 4013</div>
</section>

<section class="signature" style="top:894px">
  <div class="building-deco" role="img" aria-label="Faint green city building illustration"></div>
  <div class="brand"><span class="brand-mark"></span><span class="brand-name">Vantoq</span></div>
  <div class="person">
    <h2 class="person-name">Hugh Fenwick</h2>
    <p class="person-role">Commercial Manager</p>
    <ul class="contact-list">
      <li class="contact-item"><svg class="contact-icon"><use href="#icon-phone"/></svg>0417 352 609</li>
      <li class="contact-item"><svg class="contact-icon"><use href="#icon-mail"/></svg>hugh.fenwick@vantoq.com.au</li>
      <li class="contact-item"><svg class="contact-icon"><use href="#icon-web"/></svg>www.vantoq.com.au</li>
    </ul>
  </div>
  <svg class="bands" width="740" height="248"><use href="#signature-bands"/></svg>
  <div class="hotline"><span class="hotline-number">1300 462 318</span><span class="social-box"></span><span class="social-box"></span><span class="social-box"></span></div>
  <div class="address"><svg width="20" height="20"><use href="#icon-pin"/></svg>14/205 Carrick Road, Northgate QLD 4013</div>
</section>

</body>
</html>
```